Brimble Diecast Torvel Collectables Website

looking for a vibrant web site marketplace built for diecast car enthusiasts to buy, sell, and trade with ease. Whether you're looking to showcase your own collection or discover rare and exciting models, our site makes the process simple and enjoyable. Clients can browse a curated inventory of high‑quality diecast cars, connect with fellow collectors, and find the perfect pieces to expand their collection. With a smooth user experience and a community-driven spirit, we’re the go‑to destination for anyone passionate about diecast cars.

Target Market(s)

diecast collectors

Industry/Entity Type

Diecast Collectables

Coding

Coded - Design and coding required

Number of Pages Required

3 page

Font styles to use
Sans Serif

Colors
EE7325
F08F49
F5BC92
FAE3D3
FDF4ED

Requirements
Must have
• Cool look and feel. Woo commerce page to post and sell my inventory
Nice to have
• page for users to post their cars or looking for trades.
Should not have
• look cheap

```html
<!DOCTYPE html>
<html lang="en">
<head>
<meta charset="utf-8">
<title>Brimble Diecast – Marketplace for Miniature Masterpieces</title>
<link href="https://fonts.googleapis.com/css2?family=Lexend:wght@300;400;500;600&display=swap" rel="stylesheet">
<style>
:root{
  --orange:#EE7325;
  --orange-2:#F08F49;
  --peach:#F5BC92;
  --cream:#FAE3D3;
  --ivory:#FDF4ED;
  --gold:#E9C98C;
  --green:#5F8A4B;
  --ink:#1c1c1c;
  --text:#3a3a3a;
  --muted:#6b6b6b;
  --grey-bg:#EFEFF1;
  --footer:#222222;
  --footer-line:#4a4a4a;
}
*{box-sizing:border-box;margin:0;padding:0}
html,body{width:1200px;height:3464px;overflow:hidden}
body{font-family:"Lexend",sans-serif;color:var(--ink);background:#fff;position:relative}
.abs{position:absolute}
.hl{background:var(--gold);padding:0 7px}
.btn{position:absolute;background:var(--orange);color:#fff;font-size:12px;font-weight:500;letter-spacing:.3px;display:flex;align-items:center;justify-content:center;text-transform:uppercase}

.hero-bg{left:0;top:0;width:1200px;height:542px;background:var(--grey-bg)}
.hero-photo{left:538px;top:128px;width:662px;height:390px;background:radial-gradient(ellipse at 55% 55%,#c84a3c 0%,#3c7fa8 30%,#e8e8ea 62%,#f0f0f2 100%)}
.nav{top:58px;font-size:10px;font-weight:500;display:flex;gap:25px;text-transform:uppercase}
.nav .home{width:12px;height:12px}
.brand{left:556px;top:14px;width:88px;height:108px;display:flex;flex-direction:column;align-items:center;justify-content:center;gap:6px}
.brand .dot{width:46px;height:46px;border-radius:50%;background:var(--orange)}
.brand span{font-size:12px;font-weight:600;color:var(--ink);text-align:center;line-height:1.1}
.icons{left:866px;top:56px;display:flex;gap:12px}
.icons svg{width:15px;height:15px;stroke:var(--ink);fill:none;stroke-width:1.6}
.cart{position:relative}
.cart b{position:absolute;right:-6px;top:-5px;width:10px;height:10px;border-radius:50%;background:var(--orange);color:#fff;font-size:7px;font-weight:500;display:flex;align-items:center;justify-content:center}
.eyebrow{left:127px;top:193px;font-size:12px;color:var(--text);letter-spacing:.2px}
.hero-title{left:127px;top:218px;font-size:35px;font-weight:600;line-height:39px;color:var(--ink)}
.hero-copy{left:127px;top:318px;font-size:13px;line-height:20px;width:420px;color:var(--ink)}
.cat{top:480px;width:304px;height:145px;background:#fff;padding:7px;box-shadow:0 2px 8px rgba(0,0,0,.06)}
.cat .ph{width:100%;height:100%;position:relative}
.cat h3{position:absolute;top:18px;left:0;right:0;text-align:center;font-size:13px;font-weight:500}
.cat h3 em{font-style:normal;color:var(--orange)}

.sec-title{left:0;width:1200px;text-align:center;font-size:25px;font-weight:500}
.sec-title .hl{font-weight:600}

.card{position:absolute;width:226px;height:294px;background:#fff;box-shadow:0 2px 10px rgba(0,0,0,.07)}
.card .ph{position:absolute;left:6px;top:6px;width:214px;height:126px}
.card h4{position:absolute;left:16px;top:146px;font-size:12.5px;font-weight:500}
.card .spec{position:absolute;left:16px;top:169px;font-size:11px;line-height:17px;color:var(--text);font-weight:300}
.card .price{position:absolute;left:16px;top:214px;font-size:13.5px;font-weight:600}
.card .acts{position:absolute;right:14px;top:216px;display:flex;gap:11px}
.card .acts svg{width:14px;height:14px;stroke:var(--ink);fill:none;stroke-width:1.5}
.card .b{position:absolute;top:245px;width:94px;height:28px;color:#fff;font-size:11px;font-weight:500;display:flex;align-items:center;justify-content:center}
.card .buy{left:15px;background:var(--green)}
.card .trade{left:116px;background:var(--orange)}
.arrow{position:absolute;width:44px;height:44px;border-radius:50%;background:#c9c9c9;display:flex;align-items:center;justify-content:center}
.arrow svg{width:14px;height:14px;stroke:#fff;fill:none;stroke-width:2}

.about-bg{left:0;top:1185px;width:1200px;height:472px;background:var(--grey-bg)}
.about-title{left:696px;top:1309px;font-size:35px;font-weight:600;line-height:40px}
.about-copy{left:696px;top:1408px;width:380px;font-size:13px;line-height:20px}

.art-bg{left:0;top:2527px;width:1200px;height:587px;background:var(--grey-bg)}
.feature{left:121px;top:2653px;width:420px;height:398px;border-radius:10px;overflow:hidden;background:linear-gradient(160deg,#27424f 0%,#3d3020 35%,#b8661f 55%,#2a2218 80%,#121212 100%)}
.feature .txt{position:absolute;left:24px;bottom:28px;width:370px;color:#fff}
.feature .date{font-size:11px;color:#ddd}
.feature h3{font-size:14px;font-weight:500;color:var(--orange-2);margin:8px 0 6px}
.feature p{font-size:12px;line-height:18px;color:#eee;font-weight:300}
.more{display:flex;align-items:center;gap:6px;font-size:11.5px;font-weight:500;margin-top:22px}
.more svg{width:16px;height:16px;stroke:currentColor;fill:none;stroke-width:1.5}
.post{position:absolute;left:585px;width:480px;height:110px}
.post .ph{position:absolute;left:0;top:0;width:108px;height:105px}
.post .body{position:absolute;left:124px;top:0;width:360px}
.post .date{font-size:10.5px;color:var(--text)}
.post h4{font-size:13.5px;font-weight:500;color:var(--orange);margin:6px 0 5px}
.post p{font-size:12px;line-height:18px;color:var(--text);font-weight:300}
.post .more{margin-top:8px;font-size:10.5px;gap:5px}
.post .more svg{width:13px;height:13px}

.footer{left:0;top:3114px;width:1200px;height:350px;background:var(--footer);color:#bdbdbd}
.f-brand{left:128px;top:66px;width:86px;height:104px;display:flex;flex-direction:column;align-items:center;justify-content:center;gap:6px}
.f-brand .dot{width:44px;height:44px;border-radius:50%;background:var(--orange)}
.f-brand span{font-size:11.5px;font-weight:600;color:#fff;text-align:center;line-height:1.1}
.fcol{top:66px}
.fcol h5{font-size:10px;font-weight:500;color:var(--orange);letter-spacing:.4px;padding-bottom:9px;border-bottom:1px solid var(--footer-line);margin-bottom:14px}
.fcol ul{list-style:none;font-size:9.5px;line-height:17px;font-weight:300}
.contact li{display:flex;gap:7px;margin-bottom:20px;line-height:16px}
.contact svg{width:10px;height:10px;fill:var(--orange);flex:none;margin-top:3px}
.news{left:862px;top:64px;width:208px;height:126px;background:var(--orange);border-radius:14px;padding:20px 18px;color:#fff}
.news p{font-size:9px;font-weight:500;line-height:12.5px}
.news .field{margin-top:12px;height:30px;border:1.5px solid #fff;border-radius:15px;display:flex;align-items:center;justify-content:space-between;padding:0 10px 0 14px;font-size:10px}
.news .field svg{width:16px;height:16px;fill:#fff}
.f-line{left:126px;top:259px;width:946px;height:1px;background:var(--footer-line)}
.socials{left:126px;top:275px;display:flex;gap:10px}
.socials i{width:12px;height:12px;border-radius:50%;background:#bdbdbd;display:block}
.copy{right:128px;top:276px;font-size:8.5px;letter-spacing:.3px}
</style>
</head>
<body>

<div class="abs hero-bg"></div>
<div class="abs hero-photo" role="img" aria-label="Red, blue and yellow classic diecast model cars on a light studio background"></div>

<nav class="abs nav" style="left:258px">
  <svg class="home" viewBox="0 0 24 24"><path d="M3 11 12 3l9 8v10h-6v-6H9v6H3z" fill="#E9B94F"/></svg>
  <span>Buy</span><span>Sell</span><span>Trade</span><span>Community</span>
</nav>
<div class="abs brand"><div class="dot"></div><span>Brimble Diecast</span></div>
<nav class="abs nav" style="left:708px"><span>Blog</span><span>Contact</span></nav>
<div class="abs icons">
  <svg viewBox="0 0 24 24"><circle cx="12" cy="8" r="4"/><path d="M4 21c1-4 4-6 8-6s7 2 8 6"/></svg>
  <svg viewBox="0 0 24 24"><circle cx="11" cy="11" r="7"/><path d="m16 16 5 5"/></svg>
  <svg viewBox="0 0 24 24"><path d="M12 20S3 14 3 8.5A4.5 4.5 0 0 1 12 6a4.5 4.5 0 0 1 9 2.5C21 14 12 20 12 20z"/></svg>
  <span class="cart"><svg viewBox="0 0 24 24"><path d="M5 8h14l-1 13H6z"/><path d="M9 8V6a3 3 0 0 1 6 0v2"/></svg><b>0</b></span>
</div>

<p class="abs eyebrow">WELCOME TO BRIMBLE DIECAST</p>
<h1 class="abs hero-title">Your Marketplace for<br>Miniature <span class="hl">Masterpieces</span></h1>
<p class="abs hero-copy">Explore a growing marketplace where you can buy, sell, or trade your favorite models with collectors from around the world.</p>
<a class="btn" style="left:126px;top:377px;width:190px;height:33px">Browse our inventory</a>

<div class="abs cat" style="left:126px"><div class="ph" role="img" aria-label="Open hand holding a red diecast car" style="background:linear-gradient(100deg,#d9d9db,#f2f2f2 45%,#e3e3e5)"><h3><em>Buying</em> Diecast</h3></div></div>
<div class="abs cat" style="left:443px"><div class="ph" role="img" aria-label="Fingers holding a small red model plane" style="background:linear-gradient(100deg,#e6e6e8,#f5f5f6 50%,#e9e9eb)"><h3><em>Selling</em> Diecast</h3></div></div>
<div class="abs cat" style="left:757px"><div class="ph" role="img" aria-label="Hand passing a red diecast car over another hand" style="background:linear-gradient(100deg,#b8a8a0,#e6e6e8 40%,#f2f2f2)"><h3><em>Trading</em> Diecast</h3></div></div>

<h2 class="abs sec-title" style="top:690px">Featured <span class="hl">Diecasts</span></h2>
<div class="arrow" style="left:63px;top:878px"><svg viewBox="0 0 24 24"><path d="m15 5-7 7 7 7"/></svg></div>
<div class="arrow" style="left:1092px;top:878px"><svg viewBox="0 0 24 24"><path d="m9 5 7 7-7 7"/></svg></div>

<div class="card" style="left:126px;top:753px"><div class="ph" role="img" aria-label="Orange and teal streamlined classic model car" style="background:radial-gradient(ellipse at 50% 55%,#e2542c 0%,#e98a6c 30%,#f4f4f4 70%)"></div><h4>1960 Calloway Estella</h4><p class="spec">Diecast Size : 1:45<br>Made by : Korvane</p><p class="price">USD 39.50</p><div class="acts"><svg viewBox="0 0 24 24"><circle cx="12" cy="12" r="9"/><path d="M12 11v6M12 7.5v.5"/></svg><svg viewBox="0 0 24 24"><path d="M12 20S3 14 3 8.5A4.5 4.5 0 0 1 12 6a4.5 4.5 0 0 1 9 2.5C21 14 12 20 12 20z"/></svg><svg viewBox="0 0 24 24"><path d="M5 8h14l-1 13H6z"/><path d="M9 8V6a3 3 0 0 1 6 0v2"/></svg></div><a class="b buy">BUY</a><a class="b trade">TRADE</a></div>
<div class="card" style="left:366px;top:753px"><div class="ph" role="img" aria-label="Grey-blue vintage model sedan" style="background:radial-gradient(ellipse at 50% 55%,#6d8a96 0%,#a8bcc4 30%,#f1f2f2 70%)"></div><h4>1960 Calloway Estella</h4><p class="spec">Diecast Size : 1:45<br>Made by : Korvane</p><p class="price">USD 39.50</p><div class="acts"><svg viewBox="0 0 24 24"><circle cx="12" cy="12" r="9"/><path d="M12 11v6M12 7.5v.5"/></svg><svg viewBox="0 0 24 24"><path d="M12 20S3 14 3 8.5A4.5 4.5 0 0 1 12 6a4.5 4.5 0 0 1 9 2.5C21 14 12 20 12 20z"/></svg><svg viewBox="0 0 24 24"><path d="M5 8h14l-1 13H6z"/><path d="M9 8V6a3 3 0 0 1 6 0v2"/></svg></div><a class="b buy">BUY</a><a class="b trade">TRADE</a></div>
<div class="card" style="left:607px;top:753px"><div class="ph" role="img" aria-label="Red boxy off-road model vehicle" style="background:radial-gradient(ellipse at 50% 55%,#e33a24 0%,#ee8877 30%,#f7f7f7 70%)"></div><h4>1960 Calloway Estella</h4><p class="spec">Diecast Size : 1:45<br>Made by : Korvane</p><p class="price">USD 39.50</p><div class="acts"><svg viewBox="0 0 24 24"><circle cx="12" cy="12" r="9"/><path d="M12 11v6M12 7.5v.5"/></svg><svg viewBox="0 0 24 24"><path d="M12 20S3 14 3 8.5A4.5 4.5 0 0 1 12 6a4.5 4.5 0 0 1 9 2.5C21 14 12 20 12 20z"/></svg><svg viewBox="0 0 24 24"><path d="M5 8h14l-1 13H6z"/><path d="M9 8V6a3 3 0 0 1 6 0v2"/></svg></div><a class="b buy">BUY</a><a class="b trade">TRADE</a></div>
<div class="card" style="left:846px;top:753px"><div class="ph" role="img" aria-label="Silver-blue classic gullwing model coupe" style="background:radial-gradient(ellipse at 50% 55%,#8fb0bf 0%,#bfd0d8 35%,#ebeeef 70%)"></div><h4>1960 Calloway Estella</h4><p class="spec">Diecast Size : 1:45<br>Made by : Korvane</p><p class="price">USD 39.50</p><div class="acts"><svg viewBox="0 0 24 24"><circle cx="12" cy="12" r="9"/><path d="M12 11v6M12 7.5v.5"/></svg><svg viewBox="0 0 24 24"><path d="M12 20S3 14 3 8.5A4.5 4.5 0 0 1 12 6a4.5 4.5 0 0 1 9 2.5C21 14 12 20 12 20z"/></svg><svg viewBox="0 0 24 24"><path d="M5 8h14l-1 13H6z"/><path d="M9 8V6a3 3 0 0 1 6 0v2"/></svg></div><a class="b buy">BUY</a><a class="b trade">TRADE</a></div>

<a class="btn" style="left:553px;top:1087px;width:94px;height:33px">View all</a>

<div class="abs about-bg"></div>
<div class="abs" role="img" aria-label="Cupped hands holding a green vintage model station wagon" style="left:126px;top:1247px;width:228px;height:348px;background:linear-gradient(180deg,#ececef 0%,#e3d7cf 55%,#d9c2b4 100%)"></div>
<div class="abs" role="img" aria-label="Rows of colourful classic diecast cars on white" style="left:379px;top:1185px;width:158px;height:221px;background:linear-gradient(150deg,#e46a4c,#5aa1c9 35%,#f2a637 60%,#e9e9e9 85%)"></div>
<div class="abs" role="img" aria-label="Child playing with small toy cars at a table" style="left:379px;top:1431px;width:221px;height:164px;background:linear-gradient(135deg,#b9c3cf,#d8cfc7 50%,#f1f1f1)"></div>
<h2 class="abs about-title">The Ultimate Hub for<br>Diecast <span class="hl">Collectors</span></h2>
<p class="abs about-copy">We bring together passionate collectors and high quality diecast cars in one trusted space. Whether you're hunting for rare finds or looking to give your collection a new home, our platform makes every transaction smooth and secure.</p>
<a class="btn" style="left:694px;top:1505px;width:168px;height:34px">List your own cars</a>

<h2 class="abs sec-title" style="top:1723px">Latest <span class="hl">Diecasts</span> Collection</h2>

<div class="card" style="left:126px;top:1786px"><div class="ph" role="img" aria-label="Yellow wedge-shaped sports model car" style="background:radial-gradient(ellipse at 50% 55%,#f5c400 0%,#f1dc7a 30%,#e9e9e9 70%)"></div><h4>1960 Calloway Estella</h4><p class="spec">Diecast Size : 1:45<br>Made by : Korvane</p><p class="price">USD 39.50</p><div class="acts"><svg viewBox="0 0 24 24"><circle cx="12" cy="12" r="9"/><path d="M12 11v6M12 7.5v.5"/></svg><svg viewBox="0 0 24 24"><path d="M12 20S3 14 3 8.5A4.5 4.5 0 0 1 12 6a4.5 4.5 0 0 1 9 2.5C21 14 12 20 12 20z"/></svg><svg viewBox="0 0 24 24"><path d="M5 8h14l-1 13H6z"/><path d="M9 8V6a3 3 0 0 1 6 0v2"/></svg></div><a class="b buy">BUY</a><a class="b trade">TRADE</a></div>
<div class="card" style="left:366px;top:1786px"><div class="ph" role="img" aria-label="White rally model SUV with red stripes" style="background:radial-gradient(ellipse at 50% 55%,#f4f4f4 0%,#bcbcbc 35%,#dcdcdc 70%)"></div><h4>1960 Calloway Estella</h4><p class="spec">Diecast Size : 1:45<br>Made by : Korvane</p><p class="price">USD 39.50</p><div class="acts"><svg viewBox="0 0 24 24"><circle cx="12" cy="12" r="9"/><path d="M12 11v6M12 7.5v.5"/></svg><svg viewBox="0 0 24 24"><path d="M12 20S3 14 3 8.5A4.5 4.5 0 0 1 12 6a4.5 4.5 0 0 1 9 2.5C21 14 12 20 12 20z"/></svg><svg viewBox="0 0 24 24"><path d="M5 8h14l-1 13H6z"/><path d="M9 8V6a3 3 0 0 1 6 0v2"/></svg></div><a class="b buy">BUY</a><a class="b trade">TRADE</a></div>
<div class="card" style="left:607px;top:1786px"><div class="ph" role="img" aria-label="Orange open-top supercar model" style="background:radial-gradient(ellipse at 50% 55%,#f08a14 0%,#f3c37e 30%,#f1f1f1 70%)"></div><h4>1960 Calloway Estella</h4><p class="spec">Diecast Size : 1:45<br>Made by : Korvane</p><p class="price">USD 39.50</p><div class="acts"><svg viewBox="0 0 24 24"><circle cx="12" cy="12" r="9"/><path d="M12 11v6M12 7.5v.5"/></svg><svg viewBox="0 0 24 24"><path d="M12 20S3 14 3 8.5A4.5 4.5 0 0 1 12 6a4.5 4.5 0 0 1 9 2.5C21 14 12 20 12 20z"/></svg><svg viewBox="0 0 24 24"><path d="M5 8h14l-1 13H6z"/><path d="M9 8V6a3 3 0 0 1 6 0v2"/></svg></div><a class="b buy">BUY</a><a class="b trade">TRADE</a></div>
<div class="card" style="left:846px;top:1786px"><div class="ph" role="img" aria-label="Black muscle car model with orange stripes" style="background:radial-gradient(ellipse at 50% 55%,#2a2a30 0%,#7d7f88 35%,#eceef2 72%)"></div><h4>1960 Calloway Estella</h4><p class="spec">Diecast Size : 1:45<br>Made by : Korvane</p><p class="price">USD 39.50</p><div class="acts"><svg viewBox="0 0 24 24"><circle cx="12" cy="12" r="9"/><path d="M12 11v6M12 7.5v.5"/></svg><svg viewBox="0 0 24 24"><path d="M12 20S3 14 3 8.5A4.5 4.5 0 0 1 12 6a4.5 4.5 0 0 1 9 2.5C21 14 12 20 12 20z"/></svg><svg viewBox="0 0 24 24"><path d="M5 8h14l-1 13H6z"/><path d="M9 8V6a3 3 0 0 1 6 0v2"/></svg></div><a class="b buy">BUY</a><a class="b trade">TRADE</a></div>

<div class="card" style="left:126px;top:2096px"><div class="ph" role="img" aria-label="Pink and gold angular supercar model" style="background:radial-gradient(ellipse at 50% 55%,#d98aa0 0%,#e7c2c6 30%,#d9d9db 72%)"></div><h4>1960 Calloway Estella</h4><p class="spec">Diecast Size : 1:45<br>Made by : Korvane</p><p class="price">USD 39.50</p><div class="acts"><svg viewBox="0 0 24 24"><circle cx="12" cy="12" r="9"/><path d="M12 11v6M12 7.5v.5"/></svg><svg viewBox="0 0 24 24"><path d="M12 20S3 14 3 8.5A4.5 4.5 0 0 1 12 6a4.5 4.5 0 0 1 9 2.5C21 14 12 20 12 20z"/></svg><svg viewBox="0 0 24 24"><path d="M5 8h14l-1 13H6z"/><path d="M9 8V6a3 3 0 0 1 6 0v2"/></svg></div><a class="b buy">BUY</a><a class="b trade">TRADE</a></div>
<div class="card" style="left:366px;top:2096px"><div class="ph" role="img" aria-label="Grey-blue vintage model sedan" style="background:radial-gradient(ellipse at 50% 55%,#6d8a96 0%,#a8bcc4 30%,#f1f2f2 70%)"></div><h4>1960 Calloway Estella</h4><p class="spec">Diecast Size : 1:45<br>Made by : Korvane</p><p class="price">USD 39.50</p><div class="acts"><svg viewBox="0 0 24 24"><circle cx="12" cy="12" r="9"/><path d="M12 11v6M12 7.5v.5"/></svg><svg viewBox="0 0 24 24"><path d="M12 20S3 14 3 8.5A4.5 4.5 0 0 1 12 6a4.5 4.5 0 0 1 9 2.5C21 14 12 20 12 20z"/></svg><svg viewBox="0 0 24 24"><path d="M5 8h14l-1 13H6z"/><path d="M9 8V6a3 3 0 0 1 6 0v2"/></svg></div><a class="b buy">BUY</a><a class="b trade">TRADE</a></div>
<div class="card" style="left:607px;top:2096px"><div class="ph" role="img" aria-label="Blue racing model car with red spoiler" style="background:radial-gradient(ellipse at 50% 55%,#2f8fd0 0%,#8fbfe0 32%,#f3f3f3 72%)"></div><h4>1960 Calloway Estella</h4><p class="spec">Diecast Size : 1:45<br>Made by : Korvane</p><p class="price">USD 39.50</p><div class="acts"><svg viewBox="0 0 24 24"><circle cx="12" cy="12" r="9"/><path d="M12 11v6M12 7.5v.5"/></svg><svg viewBox="0 0 24 24"><path d="M12 20S3 14 3 8.5A4.5 4.5 0 0 1 12 6a4.5 4.5 0 0 1 9 2.5C21 14 12 20 12 20z"/></svg><svg viewBox="0 0 24 24"><path d="M5 8h14l-1 13H6z"/><path d="M9 8V6a3 3 0 0 1 6 0v2"/></svg></div><a class="b buy">BUY</a><a class="b trade">TRADE</a></div>
<div class="card" style="left:846px;top:2096px"><div class="ph" role="img" aria-label="Orange and teal streamlined classic model car" style="background:radial-gradient(ellipse at 50% 55%,#e2542c 0%,#e98a6c 30%,#f4f4f4 70%)"></div><h4>1960 Calloway Estella</h4><p class="spec">Diecast Size : 1:45<br>Made by : Korvane</p><p class="price">USD 39.50</p><div class="acts"><svg viewBox="0 0 24 24"><circle cx="12" cy="12" r="9"/><path d="M12 11v6M12 7.5v.5"/></svg><svg viewBox="0 0 24 24"><path d="M12 20S3 14 3 8.5A4.5 4.5 0 0 1 12 6a4.5 4.5 0 0 1 9 2.5C21 14 12 20 12 20z"/></svg><svg viewBox="0 0 24 24"><path d="M5 8h14l-1 13H6z"/><path d="M9 8V6a3 3 0 0 1 6 0v2"/></svg></div><a class="b buy">BUY</a><a class="b trade">TRADE</a></div>

<a class="btn" style="left:553px;top:2430px;width:94px;height:33px">View all</a>

<div class="abs art-bg"></div>
<h2 class="abs sec-title" style="top:2592px">Latest <span class="hl">Articles</span></h2>

<article class="abs feature" role="img" aria-label="Glowing orange model car in a dark display box">
  <div class="txt">
    <p class="date">Oct 10, 2023</p>
    <h3>Top 10 Rare Diecast Cars Every Collector Wants</h3>
    <p>Lorem ipsum dolor sit amet, consectetur adipiscing elit, sed do eiusmod tempor incididunt ut labore et dolore magna aliqua. Ut enim ad minim veniam, quis nostrud.</p>
    <a class="more"><svg viewBox="0 0 24 24"><circle cx="12" cy="12" r="9"/><path d="M8 12h8m-3-3 3 3-3 3"/></svg>Read more</a>
  </div>
</article>

<article class="post" style="top:2661px">
  <div class="ph" role="img" aria-label="Several dark model cars scattered on white" style="background:linear-gradient(135deg,#e9e9e9,#5b4a44 40%,#a3362f 60%,#eeeeee)"></div>
  <div class="body"><p class="date">Oct 10, 2023</p><h4>How to Spot Authentic vs. Replica Diecast Models</h4><p>Lorem ipsum dolor sit amet, consectetur adipiscing elit, sed do eiusmod tempor incididunt ut labore et dolore.</p><a class="more"><svg viewBox="0 0 24 24"><circle cx="12" cy="12" r="9"/><path d="M8 12h8m-3-3 3 3-3 3"/></svg>Read more</a></div>
</article>
<article class="post" style="top:2801px">
  <div class="ph" role="img" aria-label="Row of dark model cars seen from above" style="background:linear-gradient(90deg,#d8d8d8,#3a3a3a 30%,#e2e2e2 50%,#3a3a3a 70%,#d8d8d8)"></div>
  <div class="body"><p class="date">Oct 10, 2023</p><h4>How to Spot Authentic vs. Replica Diecast Models</h4><p>Lorem ipsum dolor sit amet, consectetur adipiscing elit, sed do eiusmod tempor incididunt ut labore et dolore.</p><a class="more"><svg viewBox="0 0 24 24"><circle cx="12" cy="12" r="9"/><path d="M8 12h8m-3-3 3 3-3 3"/></svg>Read more</a></div>
</article>
<article class="post" style="top:2939px">
  <div class="ph" role="img" aria-label="Model off-road truck on a neon-lit street" style="background:linear-gradient(135deg,#d9a23c,#7a3f6b 40%,#2a3f56 70%,#1a1a22)"></div>
  <div class="body"><p class="date">Oct 10, 2023</p><h4>How to Spot Authentic vs. Replica Diecast Models</h4><p>Lorem ipsum dolor sit amet, consectetur adipiscing elit, sed do eiusmod tempor incididunt ut labore et dolore.</p><a class="more"><svg viewBox="0 0 24 24"><circle cx="12" cy="12" r="9"/><path d="M8 12h8m-3-3 3 3-3 3"/></svg>Read more</a></div>
</article>

<footer class="abs footer">
  <div class="abs f-brand"><div class="dot"></div><span>Brimble Diecast</span></div>
  <div class="abs fcol" style="left:295px;width:72px"><h5>NAVIGATION</h5><ul><li>Home</li><li>Buy</li><li>Sell</li><li>Trade</li><li>Community</li><li>Blog</li><li>Contact</li></ul></div>
  <div class="abs fcol" style="left:446px;width:120px"><h5>INVENTORY</h5><ul><li>Classic Cars</li><li>Sports Cars</li><li>Race Cars</li><li>Commercial Trucks</li><li>Construction Equipment</li><li>Military Vehicles</li></ul></div>
  <div class="abs fcol contact" style="left:644px;width:138px"><h5>CONTACT</h5><ul>
    <li><svg viewBox="0 0 24 24"><path d="M12 2a7 7 0 0 0-7 7c0 5 7 13 7 13s7-8 7-13a7 7 0 0 0-7-7zm0 9.5A2.5 2.5 0 1 1 12 6.5a2.5 2.5 0 0 1 0 5z"/></svg><span>BrimbleDiecast.com<br>48 Marigold Way<br>Fenwick, OR 97301</span></li>
    <li><svg viewBox="0 0 24 24"><path d="M6.6 10.8a15 15 0 0 0 6.6 6.6l2.2-2.2a1 1 0 0 1 1-.25 11 11 0 0 0 3.6.6 1 1 0 0 1 1 1V20a1 1 0 0 1-1 1A17 17 0 0 1 3 4a1 1 0 0 1 1-1h3.5a1 1 0 0 1 1 1 11 11 0 0 0 .6 3.6 1 1 0 0 1-.25 1z"/></svg><span>+800.555.0192</span></li>
    <li><svg viewBox="0 0 24 24"><path d="M2 5h20v14H2zm2 2v.5l8 5 8-5V7l-8 5z"/></svg><span>info@brimblediecast.com</span></li>
  </ul></div>
  <div class="abs news">
    <p>Please subscribe to our newsletter to get the latest updates and news promotion from us.</p>
    <div class="field"><span>E-mail</span><svg viewBox="0 0 24 24"><path d="M3 3l19 9-19 9 4-9z"/></svg></div>
  </div>
  <div class="abs f-line"></div>
  <div class="abs socials"><i></i><i></i><i></i><i></i></div>
  <p class="abs copy">COPYRIGHT © 2026 BRIMBLEDIECAST.COM</p>
</footer>

</body>
</html>
```